Letterhead & logo design project

We need a letterhead for a new company called Brackenwold Ltd a firm of Chartered Accountants and Chartered Tax Advisers based in Pangbourne, Berkshire
Updates
Please include the following:
Chartered Accountants and Chartered Tax Advisers
Industry/Entity Type
It Company
Requirements
Must have
- Must have director's name at the bottom of the letterhead. Must also contain some wording at the bottom of the page to be provided by the NPRFA at a later date

```html
<!DOCTYPE html>
<html lang="en">
<head>
<meta charset="utf-8">
<title>Brackenwold Ltd – Letterhead</title>
<link href="https://fonts.googleapis.com/css2?family=PT+Sans:wght@700&family=Noto+Serif:ital,wght@0,400;0,700;1,400&display=swap" rel="stylesheet">
<style>
  :root {
    --brand-red: #d0163f;
    --ink-dark: #2b2b2e;
    --ink-grey: #4d4d52;
    --ink-soft: #6a6a70;
    --paper: #ffffff;
    --backdrop: #e9e9ec;
  }
  html, body {
    margin: 0;
    width: 1200px;
    height: 1000px;
    overflow: hidden;
    background: var(--backdrop);
  }
  .letterhead {
    position: absolute;
    left: 270px;
    top: 34px;
    width: 660px;
    height: 933px;
    background: var(--paper);
    box-shadow: 0 2px 10px rgba(0,0,0,0.12);
    overflow: hidden;
  }
  .letterhead__art {
    position: absolute;
    inset: 0;
    width: 660px;
    height: 933px;
  }
  .brand-name {
    position: absolute;
    left: 34px;
    top: 36px;
    margin: 0;
    font-family: "PT Sans", sans-serif;
    font-weight: 700;
    font-size: 25px;
    letter-spacing: 0.5px;
    text-transform: uppercase;
    color: var(--paper);
  }
  .brand-address {
    position: absolute;
    left: 34px;
    top: 76px;
    margin: 0;
    font-family: "Noto Serif", serif;
    font-size: 14px;
    letter-spacing: 0.6px;
    text-transform: uppercase;
    color: var(--ink-dark);
  }
  .services {
    position: absolute;
    right: 30px;
    top: 208px;
    margin: 0;
    text-align: right;
    font-family: "PT Sans", sans-serif;
    font-weight: 700;
    font-size: 16px;
    line-height: 1.3;
    color: var(--ink-grey);
  }
  .signatory {
    position: absolute;
    left: 34px;
    top: 676px;
  }
  .signatory__name {
    margin: 0;
    font-family: "Noto Serif", serif;
    font-weight: 700;
    font-size: 17px;
    color: var(--ink-dark);
  }
  .signatory__role {
    margin: 0;
    font-family: "Noto Serif", serif;
    font-style: italic;
    font-size: 14px;
    color: var(--ink-soft);
  }
  .tagline {
    position: absolute;
    left: 452px;
    top: 880px;
    margin: 0;
    font-family: "Noto Serif", serif;
    font-weight: 700;
    font-size: 16px;
    color: var(--paper);
    transform: rotate(3deg);
    transform-origin: left center;
  }
</style>
</head>
<body>
  <main class="letterhead">
    <svg class="letterhead__art" viewBox="0 0 660 933" aria-hidden="true">
      <!-- header band -->
      <path class="header-band" d="M0 30 H290 L400 100 Q240 72 0 68 Z" fill="var(--brand-red)"/>
      <!-- services stripes -->
      <rect x="560" y="184" width="100" height="4" fill="var(--ink-grey)"/>
      <rect x="560" y="192" width="100" height="4" fill="var(--brand-red)"/>
      <rect x="560" y="200" width="100" height="4" fill="var(--ink-dark)"/>
      <!-- signatory stripes -->
      <rect x="0" y="726" width="82" height="5" fill="var(--ink-dark)"/>
      <rect x="0" y="736" width="82" height="5" fill="var(--brand-red)"/>
      <rect x="0" y="746" width="82" height="5" fill="var(--ink-dark)"/>
      <!-- footer swoosh -->
      <path class="footer-swoosh" d="M318 786 C360 842 480 866 660 868 V912 H560 C440 906 350 862 318 786 Z" fill="var(--brand-red)"/>
    </svg>

    <h1 class="brand-name">Brackenwold Ltd.</h1>
    <p class="brand-address">Larkmere, Wessexshire</p>

    <p class="services">Chartered Accountants and<br>Chartered Tax Publishers</p>

    <div class="signatory">
      <p class="signatory__name">Your Name</p>
      <p class="signatory__role">Director</p>
    </div>

    <p class="tagline">Some tagline goes here</p>
  </main>
</body>
</html>
```